Crowdsourced IT recruitment agency - velmorix

We need an engaging and smart website design for VELMORIX Crowd recruitment. We are young innovative IT recruitment company. We have deep expertise in all IT & digital areas and using crowdsourcing to search the best market candidates faster than ever.
Our mission: to connect people and organizations interests, inspiring each other and enabling together reach better results.

We would like the design to be personalized, emotional, yet simple and neat. It should focus on the person with a problem which we solve.

Reading the site customers should feel safe and confident that velmorix is the trusted partner and everything we do is a quality product.

We also focus on long term relationship with our clients.

We have 4 products:
IT Recruitment – professional recruitment of candidates in IT and digital areas
IT RPO – candidates research process outsourcing(RPO) - provision of resume pools for the client
Kestrel Talent School – training, seminars and networking events for HR professionals from IT and hi-tech companies
Plumview Board – a tool for data visualization in nice and interactive dashboards. It pulls data from different corporate sources (SAP, Oracle, excel, etc.). It looks like a dashboard, on which there are several graphs or diagrams with HR and business KPIs(key performance indicators)

We like material design sites but also open for other options/ideas

Current site velmorix-hire.ru

Examples of websites that we like:
http://www.quobrant.ru
https://dunmirecardio.ru

Site structure:
About us (description, mission, team, clients, office)
Products: Plumview Board, HR IPO, It Recruitment
Kestrel Talent School (list of events (past and future) with the ability to upload photos, descriptions, etc.)
News: Publications, Articles, Blog
Contacts

Industry/Entity Type

Consulting

Number of Pages Required

5+ page

Font styles to use
Serif
Sans Serif

Requirements
Must have
• Individual blocks with the transition to a separate page for each product
• Link to social network (fb, link),
• Subscribe to news on the main page
• Feedback form
• Site structure:
• About us (description, mission, team, clients, office)
• Products: Plumview Board, HR IPO, It Recruitment
• Kestrel Talent School (list of events (past and future) with the ability to upload photos, descriptions, etc.)
• News: Publications, Articles, Blog, Calendars
• Contacts
Should not have
• too crowded
• too complicatied
• without advertising banners
• crammed

```html
<!DOCTYPE html>
<html lang="en">
<head>
<meta charset="utf-8">
<title>velmorix — Crowd recruitment</title>
<link href="https://fonts.googleapis.com/css2?family=Arvo:wght@400;700&family=Open+Sans:wght@400;600;700&display=swap" rel="stylesheet">
<style>
:root{
  --brand:#a1197f;
  --brand-dark:#820d5e;
  --brand-deep:#5c0a44;
  --ink:#1d1d1f;
  --muted:#9a9a9a;
  --soft:#f3f3f3;
  --white:#ffffff;
  --serif:'Arvo', Georgia, serif;
  --sans:'Open Sans', Arial, sans-serif;
}
*{margin:0;padding:0;box-sizing:border-box}
html,body{width:1200px;height:3279px;overflow:hidden}
body{position:relative;background:var(--white);font-family:var(--sans);color:var(--ink)}
.abs{position:absolute}

/* Hero */
.hero{position:absolute;left:0;top:0;width:1200px;height:800px;overflow:hidden}
.hero-photo{position:absolute;inset:0;background:
  radial-gradient(ellipse at 60% 45%, #6d3a6a 0%, #4a2a4c 35%, transparent 70%),
  linear-gradient(160deg,#5b5553 0%,#3b3236 40%,#4d2a55 75%,#2c1c33 100%)}
.hero-shade{position:absolute;inset:0;background:linear-gradient(90deg,rgba(40,10,40,.55) 0%,rgba(40,10,40,.15) 50%,rgba(40,10,40,.35) 100%)}
.sidebar{position:absolute;left:0;top:0;width:98px;height:800px;background:var(--brand-dark)}
.side-icon{position:absolute;left:29px;width:40px;height:40px}
.logo{position:absolute;left:127px;top:26px;display:flex;align-items:center;gap:12px;color:var(--white)}
.logo-dot{width:46px;height:46px;border-radius:50%;background:var(--brand)}
.logo-name{font-family:var(--sans);font-weight:700;font-size:26px;line-height:1}
.logo-tag{font-family:var(--sans);font-weight:700;font-size:9px;letter-spacing:.5px;text-transform:uppercase;margin-top:3px}
.hero-title{position:absolute;left:188px;top:154px;width:440px;font-family:var(--serif);font-size:38px;line-height:40px;color:var(--white)}
.hero-text{position:absolute;left:188px;top:334px;width:520px;font-size:14px;line-height:24px;color:var(--white)}
.btn-outline{position:absolute;left:188px;top:418px;width:262px;height:59px;border:2px solid var(--brand);color:var(--white);font-size:17px;display:flex;align-items:center;justify-content:center;letter-spacing:.5px}
.top-link{position:absolute;right:60px;top:26px;color:var(--white);font-size:11px;font-weight:600}
.page-dots{position:absolute;left:1133px;top:28px;width:12px}
.page-dots span{display:block;width:9px;height:9px;border-radius:50%;margin:0 auto 7px;background:var(--brand)}
.page-dots span:first-child{background:transparent;border:2px solid var(--white)}
.side-rule{position:absolute;left:1138px;top:0;width:1px;height:800px;background:rgba(255,255,255,.18)}
.hero-panel{position:absolute;left:909px;width:291px;height:63px;background:rgba(70,12,60,.85);display:flex;align-items:center}
.hero-panel p{flex:1;text-align:right;padding-right:22px;color:#e34ab7;font-size:13px;line-height:17px}
.hero-panel .plus{width:61px;height:63px;background:var(--brand);display:flex;align-items:center;justify-content:center}
.scroll{position:absolute;left:560px;top:714px;width:80px;text-align:center;color:var(--white);font-size:10px}

/* Sections */
.section-rule{position:absolute;left:547px;top:857px;width:104px;height:5px;background:var(--brand)}
.section-title{position:absolute;left:0;width:1200px;text-align:center;font-family:var(--serif);font-size:58px;color:var(--brand);line-height:1}
.tabs{position:absolute;left:0;width:1200px;display:flex;justify-content:center;font-size:17px;color:var(--muted)}
.tab{padding:0 0 10px;margin:0 26px}
.tab.active{color:var(--brand);border-bottom:3px solid var(--brand)}
.sub-title{position:absolute;left:0;width:1200px;text-align:center;font-family:var(--serif);font-size:30px;color:var(--ink)}
.lead{position:absolute;left:0;width:1200px;text-align:center;font-size:18px;color:var(--ink)}

.steps-line{position:absolute;left:267px;top:1296px;width:666px;border-top:2px dashed var(--brand)}
.step{position:absolute;top:1258px;width:170px;text-align:center}
.step-circle{width:76px;height:76px;margin:0 auto;border:2px dashed var(--brand);border-radius:50%;background:var(--white);display:flex;align-items:center;justify-content:center;position:relative}
.step-num{position:absolute;left:-2px;top:-8px;width:20px;height:20px;border-radius:50%;background:var(--white);border:2px dashed var(--brand);font-size:10px;color:var(--brand);display:flex;align-items:center;justify-content:center}
.step h4{font-family:var(--serif);font-weight:400;font-size:19px;margin-top:24px}
.step p{font-size:12px;line-height:19px;margin-top:8px;color:#333}
.btn-solid{position:absolute;left:372px;top:1504px;width:454px;height:61px;background:var(--brand);color:var(--white);font-size:26px;display:flex;align-items:center;justify-content:center}

.academy{position:absolute;left:0;top:1664px;width:1200px;height:430px;background:var(--soft)}
.training-photo{position:absolute;left:0;top:2094px;width:1200px;height:431px;background:linear-gradient(120deg,#cfcfcf 0%,#8d8480 35%,#5b504c 60%,#b9b2ad 100%)}
.training-card{position:absolute;left:667px;top:2127px;width:533px;height:365px;background:var(--brand);color:var(--white)}
.training-card p{position:absolute;left:67px;top:131px;width:405px;font-size:13px;line-height:20px}
.read-more{position:absolute;display:flex;align-items:center;gap:10px;font-size:13px}
.training-card .read-more{left:371px;top:262px}

.blur-tile{position:absolute;filter:blur(6px);opacity:.45}
.seminar-photo{position:absolute;left:492px;top:2590px;width:629px;height:418px;background:linear-gradient(135deg,#e9eef0 0%,#b9c3c8 40%,#6f6763 70%,#c9c1bd 100%);border:2px solid #222}
.seminar-text{position:absolute;left:57px;top:2738px;width:420px;font-size:13px;line-height:21px;color:var(--ink)}
</style>
</head>
<body>

<header class="hero">
  <div class="hero-photo" role="img" aria-label="Photo of two smiling women in business wear sitting on a purple sofa in an office"></div>
  <div class="hero-shade"></div>

  <nav class="sidebar">
    <svg class="side-icon" style="top:28px" viewBox="0 0 40 40"><g stroke="#fff" stroke-width="3"><line x1="4" y1="10" x2="36" y2="10"/><line x1="4" y1="20" x2="36" y2="20"/><line x1="4" y1="30" x2="36" y2="30"/></g></svg>
    <svg class="side-icon" style="top:130px" viewBox="0 0 40 40"><g fill="none" stroke="#fff" stroke-width="2.5"><circle cx="31" cy="8" r="5"/><circle cx="9" cy="20" r="5"/><circle cx="31" cy="32" r="5"/><line x1="13" y1="17" x2="27" y2="10"/><line x1="13" y1="23" x2="27" y2="30"/></g></svg>
    <svg class="side-icon" style="top:220px" viewBox="0 0 40 40"><g fill="none" stroke="#fff" stroke-width="2.5"><rect x="3" y="5" width="34" height="30"/><rect x="8" y="11" width="11" height="10"/><line x1="23" y1="12" x2="32" y2="12"/><line x1="23" y1="18" x2="32" y2="18"/><line x1="8" y1="25" x2="32" y2="25"/><line x1="8" y1="30" x2="32" y2="30"/></g></svg>
  </nav>

  <div class="logo">
    <span class="logo-dot"></span>
    <div><div class="logo-name">velmorix</div><div class="logo-tag">Crowd recruitment</div></div>
  </div>

  <h1 class="hero-title">Velmorix is the first crowdsourced IT recruitment agency</h1>
  <p class="hero-text">We have deep and unquie expertise in IT area using crowdsourcing to search the best market candidates faster than ever.</p>
  <a class="btn-outline">ENTER</a>

  <div class="top-link">What is velmorix</div>
  <div class="side-rule"></div>
  <div class="page-dots"><span></span><span></span><span></span><span></span><span></span></div>

  <div class="hero-panel" style="top:636px"><p>What is Crowd Recruitment<br>with velmorix?</p><div class="plus"><svg width="34" height="34" viewBox="0 0 34 34"><g stroke="#fff" stroke-width="3"><line x1="17" y1="2" x2="17" y2="32"/><line x1="2" y1="17" x2="32" y2="17"/></g></svg></div></div>
  <div class="hero-panel" style="top:702px"><p>Our mission</p><div class="plus"><svg width="34" height="34" viewBox="0 0 34 34"><g stroke="#fff" stroke-width="3"><line x1="17" y1="2" x2="17" y2="32"/><line x1="2" y1="17" x2="32" y2="17"/></g></svg></div></div>

  <div class="scroll">
    <svg width="14" height="20" viewBox="0 0 14 20"><rect x="1.5" y="1.5" width="11" height="17" rx="5.5" fill="none" stroke="#fff" stroke-width="1.5"/><line x1="7" y1="5" x2="7" y2="9" stroke="#fff" stroke-width="1.5"/></svg>
    <div>Scroll down</div>
    <svg width="16" height="24" viewBox="0 0 16 24"><g fill="none" stroke="#fff" stroke-width="1.5"><line x1="8" y1="2" x2="8" y2="21"/><polyline points="2,15 8,21 14,15"/></g></svg>
  </div>
</header>

<section class="products">
  <div class="section-rule"></div>
  <h2 class="section-title" style="top:874px">Products</h2>
  <div class="tabs" style="top:987px">
    <span class="tab active">IT Recruitment</span>
    <span class="tab">IT RPO</span>
    <span class="tab">Kestrel Talent School</span>
    <span class="tab">Plumview Board</span>
  </div>
  <h3 class="sub-title" style="top:1106px">IT Recruitment</h3>
  <p class="lead" style="top:1162px">Experienced IT recruiting professionals are welcome to join the exclusive velmorix network</p>

  <div class="steps-line"></div>
  <div class="step" style="left:182px">
    <div class="step-circle"><span class="step-num">1</span><svg width="34" height="34" viewBox="0 0 34 34" fill="none" stroke="#a1197f" stroke-width="2"><rect x="11" y="3" width="10" height="18" rx="5"/><path d="M6 16a10 10 0 0 0 20 0"/><line x1="16" y1="26" x2="16" y2="31"/></svg></div>
    <h4>Interview</h4><p>Provide the track record of your successful projects</p>
  </div>
  <div class="step" style="left:346px">
    <div class="step-circle"><span class="step-num">2</span><svg width="34" height="34" viewBox="0 0 34 34" fill="none" stroke="#a1197f" stroke-width="2"><rect x="6" y="3" width="22" height="28"/><line x1="11" y1="10" x2="23" y2="10"/><line x1="11" y1="16" x2="23" y2="16"/><line x1="11" y1="22" x2="18" y2="22"/></svg></div>
    <h4>Contract</h4><p>Complete introduction program and join the team</p>
  </div>
  <div class="step" style="left:516px">
    <div class="step-circle"><span class="step-num">3</span><svg width="34" height="34" viewBox="0 0 34 34" fill="none" stroke="#a1197f" stroke-width="2"><rect x="7" y="5" width="20" height="26"/><rect x="12" y="2" width="10" height="6"/><polyline points="11,17 15,21 23,13"/></svg></div>
    <h4>Vacancies</h4><p>Choose the projects to work and present the CVs</p>
  </div>
  <div class="step" style="left:682px">
    <div class="step-circle"><span class="step-num">4</span><svg width="34" height="34" viewBox="0 0 34 34" fill="none" stroke="#a1197f" stroke-width="2"><path d="M2 14l7-6 8 5 8-5 7 6-12 11z"/><line x1="13" y1="18" x2="17" y2="22"/></svg></div>
    <h4>CV Selection</h4><p>Receive feedback and track successfull candidates</p>
  </div>
  <div class="step" style="left:848px">
    <div class="step-circle"><span class="step-num">5</span><svg width="34" height="34" viewBox="0 0 34 34" fill="none" stroke="#a1197f" stroke-width="2"><rect x="3" y="10" width="28" height="20"/><rect x="12" y="5" width="10" height="5"/><line x1="3" y1="18" x2="31" y2="18"/></svg></div>
    <h4>Placement</h4><p>Motivate final candidate and get your free</p>
  </div>

  <a class="btn-solid">APPLY NOW</a>
</section>

<section class="academy">
  <h2 class="section-title" style="top:60px">Kestrel Talent School</h2>
  <div class="tabs" style="top:174px">
    <span class="tab active">Training</span>
    <span class="tab">Seminars</span>
    <span class="tab">Networking Events</span>
  </div>
  <h3 class="sub-title" style="top:288px">Training</h3>
  <p class="lead" style="top:347px">Experienced IT recruiting professionals are welcome to join the exclusive velmorix network</p>
</section>

<div class="training-photo" role="img" aria-label="Photo of a woman presenting to a seated group in a bright training room"></div>
<div class="training-card">
  <p>Our executive network is over 100 experienced recruiting professionals which cover IT candidates market on territory of Russia, Ukraine, Belarus, Kazakhstan and Europe. For your project we choose only respectively expertized headhunters who reach out efficiently to the talented candidates you are looking for.</p>
  <a class="read-more">Read more <svg width="24" height="14" viewBox="0 0 24 14" fill="none" stroke="#fff" stroke-width="1.6"><line x1="0" y1="7" x2="22" y2="7"/><polyline points="16,1 22,7 16,13"/></svg></a>
</div>

<div class="blur-tile" style="left:324px;top:2558px;width:195px;height:175px;background:linear-gradient(135deg,#c9cdd3,#8f8a8e)" role="img" aria-label="Faded photo of a seminar audience"></div>
<div class="blur-tile" style="left:61px;top:2838px;width:227px;height:153px;background:linear-gradient(135deg,#d8d2cf,#a59c98)" role="img" aria-label="Faded photo of a workshop table"></div>
<div class="blur-tile" style="left:354px;top:2930px;width:308px;height:208px;background:linear-gradient(135deg,#cfc7c2,#928882)" role="img" aria-label="Faded photo of a networking event"></div>

<div class="seminar-photo" role="img" aria-label="Photo of a man presenting at a whiteboard to colleagues in a meeting room"></div>
<p class="seminar-text">Depending on the specifics of particular vacancy velmorix project manager organizes smart search using such opportunities as direct search, on-line recruitment, professional referral, national and global recruitment, social networks, professional forums and networking.</p>
<a class="read-more" style="left:363px;top:2843px;color:var(--ink)">Read more <svg width="24" height="14" viewBox="0 0 24 14" fill="none" stroke="#1d1d1f" stroke-width="1.6"><line x1="0" y1="7" x2="22" y2="7"/><polyline points="16,1 22,7 16,13"/></svg></a>

</body>
</html>
```